Investment Company Business Card Design

We need a Business Card design for a new company based in Boston called "Velm Investment". We are cooperating with local real estate and construction companies. Our company is very actively and aggressively acquiring primarily residential investment properties either to buy and hold long term or for purposes or renovating and repositioning for re-sale in the market. In addition, we undertake some development projects and acquisitions as opportunities present themselves. the final design should contains information about “Velm" the river boat. we are tenacious, indomitable, and the business have a favorable wind throughout the voyage for all our investment.
sample Info. on Design:
Tusa Merrick
CEO
555-xxx-xxxx
418 Harlow St. Suite 507, Boston, MA 02111
Please provide a template also, that we can edit the info later.
Reason: i just got new LOGO Design attached will be use in Business Card Design.
Construction

```html
<!DOCTYPE html>
<html lang="en">
<head>
<meta charset="utf-8">
<title>Velm Investment — Business Card</title>
<link rel="stylesheet" href="https://fonts.googleapis.com/css2?family=Mulish:wght@400;700&display=swap">
<style>
  :root {
    --backdrop: #e4e4e4;
    --card-dark-start: #2b3f46;
    --card-dark-end: #52666b;
    --card-light: #ffffff;
    --gold: #c9a25a;
    --gold-text: #c8923f;
    --ink: #1f3340;
    --muted: #8a8f93;
    --body: #4a4f54;
  }
  * { box-sizing: border-box; margin: 0; padding: 0; }
  html, body {
    width: 1200px; height: 720px; overflow: hidden;
    background: var(--backdrop);
    font-family: "Mulish", "Century Gothic", sans-serif;
  }
  .stage { position: relative; width: 1200px; height: 720px; }
  .card {
    position: absolute; top: 241px;
    width: 420px; height: 240px;
    box-shadow: 0 10px 24px rgba(0,0,0,0.28);
  }
  .card--front {
    left: 147px;
    background: linear-gradient(200deg, var(--card-dark-end) 0%, var(--card-dark-start) 70%);
  }
  .card--back { left: 633px; background: var(--card-light); }

  .brand { display: flex; align-items: center; gap: 10px; color: var(--gold); font-weight: 400; }
  .brand__dot { width: 14px; height: 14px; border-radius: 50%; background: var(--gold); flex: none; }
  .card--front .brand {
    position: absolute; left: 0; right: 0; top: 100px;
    justify-content: center; font-size: 30px; letter-spacing: 1px;
  }
  .card--back .brand {
    position: absolute; right: 22px; top: 60px;
    font-size: 21px; letter-spacing: 0.5px;
  }

  .contact { position: absolute; left: 14px; top: 104px; }
  .contact__name { font-size: 21px; font-weight: 700; color: var(--ink); line-height: 1.1; }
  .contact__role { font-size: 12px; color: var(--muted); margin-top: 4px; letter-spacing: 0.5px; }
  .contact__details { position: absolute; left: 14px; top: 178px; color: var(--gold-text); }
  .contact__phone { font-size: 11px; line-height: 1.5; }
  .contact__address { font-size: 13px; line-height: 1.5; margin-top: 2px; }

  .motto {
    position: absolute; left: 226px; width: 190px; top: 116px;
    text-align: center; font-size: 11px; line-height: 20px; color: var(--body);
  }
</style>
</head>
<body>
  <main class="stage">
    <section class="card card--front" aria-label="Card front">
      <div class="brand"><span class="brand__dot"></span><span class="brand__name">Velm Investment</span></div>
    </section>

    <section class="card card--back" aria-label="Card back">
      <div class="brand"><span class="brand__dot"></span><span class="brand__name">Velm Investment</span></div>
      <div class="contact">
        <p class="contact__name">Tusa Merrick</p>
        <p class="contact__role">CEO</p>
      </div>
      <div class="contact__details">
        <p class="contact__phone">555-xxx-xxxx</p>
        <p class="contact__address">418 Harlow St. Suite 507, Boston, MA</p>
      </div>
      <p class="motto">we are tenacious, indomitable, and the business have a favorable wind throughout the voyage for all our investment.</p>
    </section>
  </main>
</body>
</html>
```